Need a plumber

Would like a postcard sized flyer made up. Want the design to be kept very simple.
List of services we carry out in bullet point or similar.
Phone number and email included on the flyer.
Logo to feature prominantly.

List of services: Hot water issues
Burst Pipes
Gas Plumbing
Roof leaks
Drain blockages

Target Market(s)

Mums, dads and hosehgold owners

Industry/Entity Type

Plumbing

Colors
0054AA
0677BA
7BADD7
CADEEF
E8F1F8

Requirements
Must have
• Services we off and our logo, also must say "local plumber"

```html
<!DOCTYPE html>
<html lang="en">
<head>
<meta charset="utf-8">
<title>Clearflow Plumbing – Postcard Flyer</title>
<link href="https://fonts.googleapis.com/css2?family=Poppins:ital,wght@0,400;0,500;0,600;0,700;0,800;1,600;1,800&display=swap" rel="stylesheet">
<style>
  :root {
    --backdrop: #c3c9d4;
    --card: #ffffff;
    --ink: #1f1f1f;
    --brand-blue: #0a9be4;
    --band-blue: #1e98e2;
    --band-light: #56b6ee;
    --ring: #9fd2f3;
    --bar: #222222;
    --white: #ffffff;
    --photo-light: #e7eaee;
    --photo-mid: #b9c0c8;
    --photo-dark: #6c737c;
  }
  * { margin: 0; padding: 0; box-sizing: border-box; }
  html, body { width: 784px; height: 1200px; overflow: hidden; }
  body {
    background: var(--backdrop);
    font-family: "Poppins", sans-serif;
    position: relative;
  }
  .postcard {
    position: absolute;
    left: 42px; top: 353px;
    width: 700px; height: 494px;
    background: var(--card);
    overflow: hidden;
    box-shadow: 0 10px 22px rgba(0,0,0,.28);
  }
  .hero-photo {
    position: absolute; left: 330px; top: 0; width: 370px; height: 272px;
    background: radial-gradient(ellipse at 75% 40%, var(--photo-mid), transparent 60%),
                linear-gradient(90deg, var(--card) 0%, var(--photo-light) 30%, var(--photo-mid) 70%, var(--photo-dark) 100%);
  }
  .logo {
    position: absolute; left: 31px; top: 41px; width: 98px; height: 98px;
    border: 3px solid var(--ink); border-radius: 50%;
    display: flex; align-items: center; justify-content: center;
    box-shadow: inset 0 0 0 3px var(--white), inset 0 0 0 5px var(--brand-blue);
  }
  .logo-name {
    font-weight: 600; font-size: 11px; letter-spacing: 1.5px; color: var(--ink);
  }
  .headline {
    position: absolute; left: 148px; top: 36px;
    font-weight: 800; font-style: italic; line-height: 0.98; font-size: 49px;
    letter-spacing: -1px; color: var(--ink);
  }
  .headline .accent { color: var(--brand-blue); display: block; }
  .tagline {
    position: absolute; left: 38px; top: 168px;
    font-weight: 600; font-style: italic; font-size: 17px; line-height: 22px; color: var(--ink);
  }
  .service-band {
    position: absolute; left: 0; top: 270px; width: 700px; height: 146px;
    background: linear-gradient(180deg, var(--band-blue), var(--band-light) 60%, var(--band-blue));
  }
  .service {
    position: absolute; top: 225px; width: 120px; margin-left: -60px; text-align: center;
  }
  .service-ring {
    width: 106px; height: 106px; margin: 0 auto; border-radius: 50%;
    background: var(--ring); opacity: .95;
    display: flex; align-items: center; justify-content: center;
  }
  .service-photo { width: 86px; height: 86px; border-radius: 50%; border: 2px solid var(--white); }
  .service-label {
    margin-top: 14px; font-weight: 700; font-size: 15.5px; line-height: 17px; color: var(--white);
  }
  .divider {
    position: absolute; top: 335px; height: 54px; border-left: 1px dashed rgba(255,255,255,.7);
  }
  .contact-bar {
    position: absolute; left: 33px; top: 398px; width: 629px; height: 34px;
    background: var(--bar); border-radius: 17px;
    display: flex; align-items: center; color: var(--white);
    font-size: 17px; letter-spacing: 1.4px;
  }
  .contact-icon {
    width: 24px; height: 24px; border-radius: 50%; background: var(--brand-blue);
    display: flex; align-items: center; justify-content: center; flex: none;
  }
  .contact-phone { display: flex; align-items: center; gap: 10px; margin-left: 4px; width: 211px; }
  .contact-sep { width: 1px; height: 22px; background: #777; margin-right: 28px; }
  .contact-email { display: flex; align-items: center; gap: 12px; }
  .website {
    position: absolute; left: 0; top: 440px; width: 700px; text-align: center;
    font-size: 18px; letter-spacing: 3.2px; font-weight: 500; color: var(--ink);
  }
  .website .accent { color: var(--brand-blue); font-weight: 600; }
</style>
</head>
<body>
  <main class="postcard">
    <div class="hero-photo" role="img" aria-label="Photo of a plumber in overalls fixing a kitchen tap over a sink, with pale pipework on a white wall"></div>

    <div class="logo"><span class="logo-name">CLEARFLOW</span></div>

    <h1 class="headline">Need a<span class="accent">Plumber?</span></h1>
    <p class="tagline">Hire Clearflow Plumbing for<br>Professional Plumbing Services!</p>

    <div class="service-band" role="img" aria-label="Blue band with water droplet texture"></div>

    <div class="service" style="left:87px">
      <div class="service-ring"><div class="service-photo" role="img" aria-label="Plumber servicing a hot water system" style="background:linear-gradient(135deg,#8aa6c4,#3d5f8c)"></div></div>
      <p class="service-label">Hot water<br>issues</p>
    </div>
    <div class="service" style="left:211px">
      <div class="service-ring"><div class="service-photo" role="img" aria-label="Water spraying from a burst copper pipe" style="background:linear-gradient(135deg,#a0744e,#1a1a1a 60%,#9aa4ad)"></div></div>
      <p class="service-label">Burst<br>Pipes</p>
    </div>
    <div class="service" style="left:343px">
      <div class="service-ring"><div class="service-photo" role="img" aria-label="Tradesman working on gas pipework" style="background:linear-gradient(135deg,#d8dde2,#8d97a3 60%,#3b5d85)"></div></div>
      <p class="service-label">Gas<br>Plumbing</p>
    </div>
    <div class="service" style="left:471px">
      <div class="service-ring"><div class="service-photo" role="img" aria-label="Water dripping from a leaking ceiling" style="background:linear-gradient(180deg,#c9ccce,#9c9890 55%,#b98a4f)"></div></div>
      <p class="service-label">Roof<br>leaks</p>
    </div>
    <div class="service" style="left:600px">
      <div class="service-ring"><div class="service-photo" role="img" aria-label="Plumber clearing a blocked drain under a sink" style="background:linear-gradient(135deg,#eceff2,#9aa1a8 55%,#3c3f44)"></div></div>
      <p class="service-label">Drain<br>Blockages</p>
    </div>

    <span class="divider" style="left:147px"></span>
    <span class="divider" style="left:268px"></span>
    <span class="divider" style="left:407px"></span>
    <span class="divider" style="left:535px"></span>

    <div class="contact-bar">
      <div class="contact-phone">
        <span class="contact-icon">
          <svg width="13" height="13" viewBox="0 0 24 24"><path fill="#fff" d="M6.6 10.8a15 15 0 0 0 6.6 6.6l2.2-2.2c.3-.3.7-.4 1-.2 1.1.4 2.3.6 3.6.6.6 0 1 .4 1 1V20c0 .6-.4 1-1 1A17 17 0 0 1 3 4c0-.6.4-1 1-1h3.5c.6 0 1 .4 1 1 0 1.3.2 2.5.6 3.6.1.3 0 .7-.2 1z"/></svg>
        </span>
        <span>+61412345678</span>
      </div>
      <span class="contact-sep"></span>
      <div class="contact-email">
        <span class="contact-icon">
          <svg width="13" height="13" viewBox="0 0 24 24"><rect x="3" y="6" width="18" height="12" rx="2" fill="#fff"/><path d="M3.5 7l8.5 6 8.5-6" stroke="#0a9be4" stroke-width="1.8" fill="none"/></svg>
        </span>
        <span>info@clearflowplumbers.com.au</span>
      </div>
    </div>

    <p class="website">www.<span class="accent">clearflowplumbers</span>.com.au</p>
  </main>
</body>
</html>
```